Women's Health Company needs business card

We need a business card for a USA based women's health care company. We use digital technology to enhance therapy prescribed by clinicians for their patients

```html
<!DOCTYPE html>
<html lang="en">
<head>
<meta charset="utf-8">
<title>Veloria Health – Business Card</title>
<link href="https://fonts.googleapis.com/css2?family=Poppins:ital,wght@0,300;0,400;1,300&display=swap" rel="stylesheet">
<style>
  :root {
    --backdrop: #2d2d2e;
    --card-top: #1c1d1f;
    --card-bottom: #26272a;
    --teal: #5fb3ae;
    --purple: #8e4aa0;
    --ink-light: #e4e4e4;
    --emboss: #4a4b4e;
  }
  html, body {
    margin: 0;
    width: 1200px;
    height: 1138px;
    overflow: hidden;
    background: var(--backdrop);
    font-family: "Poppins", sans-serif;
  }
  .card {
    position: absolute;
    border-radius: 16px;
    overflow: hidden;
    background: linear-gradient(160deg, var(--card-top) 0%, var(--card-bottom) 100%);
    box-shadow: 0 6px 14px rgba(0,0,0,0.35);
  }
  .card--front { left: 272px; top: 184px; width: 622px; height: 376px; }
  .card--back  { left: 274px; top: 606px; width: 620px; height: 375px; }

  .front-brand {
    position: absolute;
    left: 0; right: 0; top: 140px;
    text-align: center;
    font-weight: 300;
    font-size: 58px;
    color: var(--emboss);
    letter-spacing: 1px;
  }
  .front-web {
    position: absolute;
    left: 0; right: 0; top: 320px;
    display: flex;
    justify-content: center;
    align-items: center;
    gap: 24px;
  }
  .front-web__rule { width: 48px; height: 2px; background: var(--teal); }
  .front-web__url {
    font-weight: 300;
    font-size: 16px;
    letter-spacing: 5px;
    color: var(--purple);
  }

  .edge-dot {
    position: absolute;
    left: -22px; top: 56px;
    width: 32px; height: 56px;
    border-radius: 50%;
    background: var(--teal);
  }
  .person { position: absolute; left: 37px; top: 60px; }
  .person__name {
    margin: 0;
    font-weight: 400;
    font-size: 29px;
    line-height: 1.1;
    color: var(--teal);
  }
  .person__role {
    margin: 2px 0 0;
    font-style: italic;
    font-weight: 300;
    font-size: 17px;
    color: var(--ink-light);
  }
  .address {
    position: absolute; left: 37px; top: 202px;
    margin: 0;
    font-weight: 300;
    font-size: 16px;
    line-height: 23px;
    color: var(--ink-light);
  }
  .contacts {
    position: absolute; left: 37px; top: 267px;
    margin: 0; padding: 0; list-style: none;
    font-weight: 300;
    font-size: 16px;
    line-height: 23px;
    color: var(--ink-light);
  }
  .contacts li { display: flex; align-items: center; gap: 12px; }
  .contacts svg { width: 15px; height: 15px; fill: var(--purple); flex: none; }
  .back-brand {
    position: absolute;
    right: 40px; top: 258px;
    font-weight: 300;
    font-size: 38px;
    color: var(--teal);
  }
</style>
</head>
<body>
  <section class="card card--front">
    <div class="front-brand">Veloria Health</div>
    <div class="front-web">
      <span class="front-web__rule"></span>
      <span class="front-web__url">www.veloriahealth.com</span>
      <span class="front-web__rule"></span>
    </div>
  </section>

  <section class="card card--back">
    <span class="edge-dot"></span>
    <div class="person">
      <h1 class="person__name">Jane Miller</h1>
      <p class="person__role">Health Advisor</p>
    </div>
    <p class="address">234 Anywhere St.,<br>Any City, US 123456</p>
    <ul class="contacts">
      <li>
        <svg viewBox="0 0 16 16" aria-hidden="true"><path d="M2 4c0-1 1-2 2-2h8c1 0 2 1 2 2v1h-3V4H5v1H2z"/><path d="M4 7h8l2 6H2z"/></svg>
        00-000-0000
      </li>
      <li>
        <svg viewBox="0 0 16 16" aria-hidden="true"><path d="M1 3h14v10H1z M2.5 4.5 8 9l5.5-4.5" stroke="#1f2022" stroke-width="1"/></svg>
        jane@veloriahealth.com
      </li>
      <li>
        <svg viewBox="0 0 16 16" aria-hidden="true"><circle cx="8" cy="8" r="7"/><path d="M1 8h14M8 1v14M3 4h10M3 12h10" stroke="#1f2022" stroke-width="1" fill="none"/></svg>
        www.veloriahealth.com
      </li>
    </ul>
    <div class="back-brand">Veloria Health</div>
  </section>
</body>
</html>
```